Quelvon Corporate General Presentation

Quelvon is a leading player in ICT (Information Communication Technology) cooling, we need a design for our corporate general presentation.

Attached is a reference of content

Our logo main color is industrial blue, our technology is green (energy saving).

existing website: www.quel-von.com www.quel-von.uk

Target Market(s)

Global

Industry/Entity Type

Communication

Number of Pages Required

5+ page

Font styles to use
Serif
Sans Serif

Colors
0255a3
3176b5
0293ce
33a6d7
9bcb3c

```html
<!DOCTYPE html>
<html lang="en">
<head>
<meta charset="utf-8">
<title>Quelvon – Topic</title>
<link rel="stylesheet" href="https://fonts.googleapis.com/css2?family=Roboto+Condensed:wght@400;700&display=swap">
<style>
  :root {
    --brand-blue: #0b6ab3;
    --brand-blue-light: #2a93de;
    --ink-black: #050505;
    --paper: #ffffff;
    --footer-ink: #555a60;
    --footer-rule: #d9dde2;
    --backdrop-top: #f3f4f6;
    --backdrop-bottom: #fbfbfc;
  }
  * { margin: 0; padding: 0; box-sizing: border-box; }
  html, body { width: 1200px; height: 900px; overflow: hidden; }
  body { font-family: "Roboto Condensed", "Arial Narrow", sans-serif; background: var(--paper); }

  .slide { position: relative; width: 1200px; height: 900px; overflow: hidden; }

  .backdrop {
    position: absolute; left: 0; top: 87px; width: 1200px; height: 760px;
    background: linear-gradient(180deg, var(--backdrop-top) 0%, #eef0f2 45%, var(--backdrop-bottom) 100%);
  }

  .header { position: absolute; left: 0; top: 0; width: 1200px; height: 87px; }
  .header svg { position: absolute; inset: 0; }
  .header-title {
    position: absolute; left: 19px; top: 14px;
    color: var(--paper); font-weight: 700; font-size: 44px; letter-spacing: 0.5px;
  }
  .brand {
    position: absolute; left: 990px; top: 0; width: 190px; height: 87px;
    display: flex; align-items: center; justify-content: flex-end;
    color: var(--paper); font-weight: 700; font-size: 40px; letter-spacing: 4px; line-height: 1;
  }

  .agenda { position: absolute; left: 54px; top: 250px; width: 1089px; list-style: none; }
  .agenda-item { display: flex; height: 58px; margin-bottom: 30px; }
  .agenda-number {
    width: 60px; background: var(--ink-black); color: var(--paper);
    font-weight: 700; font-size: 27px; display: flex; align-items: center; justify-content: center;
  }
  .agenda-label {
    flex: 1; background: var(--brand-blue); color: var(--paper);
    font-weight: 700; font-size: 27px; display: flex; align-items: center; padding-left: 14px;
  }

  .footer {
    position: absolute; left: 0; top: 848px; width: 1200px; height: 52px;
    border-top: 1px solid var(--footer-rule); background: var(--paper);
    display: flex; justify-content: space-between; align-items: center;
    padding: 0 16px; color: var(--footer-ink); font-weight: 700; font-size: 16px;
  }
</style>
</head>
<body>
<div class="slide">
  <div class="backdrop" role="img" aria-label="Faded photo of a data centre aisle with server racks"></div>

  <header class="header">
    <svg width="1200" height="87" viewBox="0 0 1200 87" aria-hidden="true">
      <rect width="1200" height="87" fill="var(--brand-blue)"/>
      <polygon points="897,0 918,0 966,87 945,87" fill="var(--paper)"/>
      <polygon points="918,0 934,0 982,87 966,87" fill="var(--brand-blue-light)"/>
    </svg>
    <h1 class="header-title">TOPIC</h1>
    <div class="brand">QUELVON</div>
  </header>

  <ol class="agenda">
    <li class="agenda-item"><span class="agenda-number">01</span><span class="agenda-label">BUSINESS&nbsp; STRATEGIES</span></li>
    <li class="agenda-item"><span class="agenda-number">02</span><span class="agenda-label">ABOUT&nbsp; QUELVON</span></li>
    <li class="agenda-item"><span class="agenda-number">03</span><span class="agenda-label">PRODUCTS AND SOLUTIONS</span></li>
    <li class="agenda-item"><span class="agenda-number">04</span><span class="agenda-label">PARTNERS AND CUSTOMERS</span></li>
  </ol>

  <footer class="footer">
    <span class="footer-copyright">COPYRIGHT TEXT HERE</span>
    <span class="footer-page">PAGE : 01</span>
  </footer>
</div>
</body>
</html>
```